Mirabotta war genau die Richtige für mich. Sie hat zügig und professionell gearbeitet und ihr Entwurf hat genau meinen Geschmack getroffen. Die Kommunikation war sehr freundlich und klar.
Zielgruppe
Ich bin Systemische Coach und möchte eine Methode bewerben. Es geht dabei um Auflösung von Schocktraumata. Also Trauma nach Unfall, Gewalterfahrung, Katastrophe, Diagnose, Operation, traumatischer Geburt, etc.
Mein Flyer soll Menschen erreichen, die so etwas erlebt haben und bei denen das Ereignis immer noch getriggert wird. z.B. Polizist:innen, Rettungshelfer:innen, Ärzt:innen
Genaueres hier: www.ruhe-anker.de
Die Methode bietet schnelle Hilfe, arbeitet mit Visualisierung und Klopfen, und retraumatisiert nicht.
Aufgabenstellung
Design sollte sich an der Website orientieren. Texte können davon genommen werden.
Anbei noch ein Text, der in einem Veranstaltungsnewsletter erscheint.
Bildmaterial ebenfalls von Website (bitte dann anfragen, was gebraucht wird) oder sehr gerne auch anderes von bilder.kavomex.com
Format: Din lang, 4 Seiten, hoch oder quer ist egal

```html
<!DOCTYPE html>
<html lang="de">
<head>
<meta charset="utf-8">
<title>Anker Release Technik – Flyer DIN lang</title>
<link rel="stylesheet" href="https://fonts.googleapis.com/css2?family=Handlee&family=Roboto+Condensed:wght@400;700&display=swap">
<style>
  :root {
    --band: #8281bb;
    --band-dark: #4c519e;
    --band-light: #d3d1ea;
    --ink: #3b3f9f;
    --text: #2a2a2e;
    --paper: #ffffff;
    --paper-grey: #ededee;
    --stage: #ebebeb;
  }
  * { box-sizing: border-box; margin: 0; padding: 0; }
  html, body { width: 860px; height: 1200px; overflow: hidden; background: var(--stage); }
  .canvas { position: relative; width: 860px; height: 1200px; font-family: "Roboto Condensed", sans-serif; color: var(--text); }
  .spread { position: absolute; left: 20px; width: 819px; height: 578px; display: flex; box-shadow: 0 6px 18px rgba(0,0,0,.15); }
  .spread--outside { top: 14px; }
  .spread--inside { top: 608px; }
  .panel { position: relative; width: 273px; height: 578px; overflow: hidden; background: var(--paper); }
  .script { font-family: "Handlee", cursive; }

  /* outside */
  .top { position: absolute; left: 0; top: 0; width: 100%; height: 186px; text-align: center; }
  .band { position: absolute; left: 0; top: 186px; width: 100%; height: 118px; background: var(--band); color: #fff; text-align: center; }
  .photo { position: absolute; left: 0; top: 304px; width: 100%; height: 242px; }
  .foot { position: absolute; left: 0; bottom: 0; width: 100%; height: 32px; background: var(--band-dark); color: #fff; font-size: 13px; line-height: 32px; text-align: center; }

  .quote { color: var(--ink); font-size: 12px; line-height: 1.55; padding: 0 26px; }
  .quote cite { display: block; text-align: right; font-family: "Roboto Condensed", sans-serif; font-style: normal; font-size: 9px; }
  .quote--top { padding-top: 42px; }
  .photo .quote { padding-top: 14px; }
  .photo--flower { background: linear-gradient(180deg, #f0c98f 0%, #e8cfae 30%, #a99990 60%, #7d706a 100%); }
  .photo--beach { background: linear-gradient(180deg, #c9d1db 0%, #b7c2cc 35%, #c7b49a 55%, #b09a7e 100%); }

  .intro { color: var(--ink); font-size: 11px; line-height: 1.3; font-weight: 700; padding: 34px 20px 0; }
  .intro .script { display: block; font-weight: 400; font-size: 17px; margin: 12px 0; }
  .band-title { font-size: 26px; line-height: 1.05; padding-top: 20px; }

  .contact { position: absolute; left: 37px; top: 270px; width: 199px; height: 257px; background: var(--band-light); text-align: center; font-size: 10px; line-height: 1.35; padding-top: 18px; }
  .contact h3 { color: var(--ink); font-size: 11px; text-decoration: underline; margin-bottom: 10px; }
  .contact .name { color: var(--ink); font-size: 12px; margin-bottom: 3px; }
  .contact ul { list-style: none; display: inline-block; text-align: left; margin: 12px 0 16px; }
  .contact li { display: flex; align-items: center; gap: 6px; }
  .contact svg { width: 10px; height: 10px; fill: var(--ink); }

  .panel--cover .top { background: var(--paper-grey); }
  .brand { display: flex; flex-direction: column; align-items: center; gap: 16px; padding-top: 44px; }
  .brand-dot { width: 54px; height: 54px; border-radius: 50%; background: var(--band-light); }
  .brand-name { color: var(--ink); font-size: 20px; }
  .band-head { font-size: 14px; line-height: 1.2; padding-top: 14px; font-weight: 700; }
  .band-copy { font-size: 10px; line-height: 1.3; padding: 10px 22px 0; }

  /* inside */
  .panel--inside { background: linear-gradient(180deg, #ececee 0%, #f7f7f8 100%); }
  .frame { position: absolute; left: 0; top: 0; width: 100%; height: 124px; background: var(--band); }
  .panel--intro .frame { background: #5d5fa8; }
  .panel--detail-b .frame { background: var(--band-light); }
  .inside-photo { position: absolute; left: 12px; top: 12px; width: 249px; height: 131px; background: linear-gradient(90deg, #d9c7a6 0%, #e9e3da 35%, #eeece8 60%, #c6b8a8 100%); }
  .inside-foot { position: absolute; left: 0; bottom: 0; width: 100%; height: 26px; background: var(--band-dark); }
  .panel--intro .inside-foot { background: #3e4386; }
  .panel--detail-b .inside-foot { background: var(--band); }
  .copy { position: absolute; left: 28px; right: 26px; top: 165px; font-size: 8.6px; line-height: 1.27; text-align: justify; }
  .copy h2 { color: var(--ink); font-size: 10px; font-weight: 700; margin-bottom: 6px; text-align: left; }
  .copy p { margin-bottom: 6px; }
  .copy .lead { color: var(--ink); font-size: 9.4px; }
  .bullets { list-style: none; text-align: left; }
  .bullets li { position: relative; padding-left: 8px; margin-bottom: 5px; font-size: 8.8px; line-height: 1.27; }
  .bullets li::before { content: ""; position: absolute; left: 0; top: 4px; width: 3px; height: 3px; border-radius: 50%; background: var(--ink); }
</style>
</head>
<body>
<div class="canvas">

  <section class="spread spread--outside">
    <article class="panel panel--quotes">
      <div class="top">
        <blockquote class="quote quote--top script">
          Dass die Vögel der Sorge und des Kummers über deinem Haupt fliegen, kannst du nicht ändern. Doch du kannst verhindern, dass sie Nester in deinem Haar bauen.
          <cite>(Edvard Krumholt)</cite>
        </blockquote>
      </div>
      <div class="band"></div>
      <div class="photo photo--flower" role="img" aria-label="Foto: rosa Blume wächst aus einem Riss im Asphalt am Straßenrand im Abendlicht">
        <blockquote class="quote script">
          Erfahrung ist nicht etwas, was dir passiert; sie ist vielmehr das, was du mit dem tust, was dir passiert!
          <cite>(Ansel Marbury)</cite>
        </blockquote>
      </div>
      <div class="foot">www.ruhe-anker.de</div>
    </article>

    <article class="panel panel--contact">
      <div class="top intro">
        Sie müssen nicht mit schlimmen Erinnerungen leben und diese immer wieder durchleiden.
        <span class="script">Es gibt eine Lösung!</span>
        In einem vertraulichen Gespräch klären wir die Möglichkeiten.
      </div>
      <div class="band"><p class="band-title script">Geben Sie sich<br>eine Chance!</p></div>
      <div class="contact">
        <h3>Kontakt:</h3>
        <p class="name">Malvine Osterkamp</p>
        <p>Am Lindenhang 14<br>79000 Talheim</p>
        <ul>
          <li><svg viewBox="0 0 24 24"><path d="M6.6 10.8a15 15 0 0 0 6.6 6.6l2.2-2.2a1 1 0 0 1 1-.25 11.4 11.4 0 0 0 3.6.57 1 1 0 0 1 1 1V20a1 1 0 0 1-1 1A17 17 0 0 1 3 4a1 1 0 0 1 1-1h3.5a1 1 0 0 1 1 1c0 1.25.2 2.45.57 3.57a1 1 0 0 1-.25 1z"/></svg>+49 (0)171 24 68 135</li>
          <li><svg viewBox="0 0 24 24"><path d="M2 5h20v14H2z M2 5l10 8 10-8" fill="none" stroke="#3b3f9f" stroke-width="2"/></svg>info@ruhe-anker.de</li>
          <li><svg viewBox="0 0 24 24"><circle cx="12" cy="12" r="9" fill="none" stroke="#3b3f9f" stroke-width="1.8"/><path d="M3 12h18M12 3c3 3 3 15 0 18M12 3c-3 3-3 15 0 18" fill="none" stroke="#3b3f9f" stroke-width="1.5"/></svg>www.ruhe-anker.de</li>
        </ul>
        <h3>Praxis:</h3>
        <p class="name">Praxis am Bachlauf</p>
        <p>Birkenweg 9<br>79100 Lindenau</p>
      </div>
      <div class="foot">www.ruhe-anker.de</div>
    </article>

    <article class="panel panel--cover">
      <div class="top">
        <div class="brand">
          <span class="brand-dot"></span>
          <span class="brand-name">Anker Release Technik</span>
        </div>
      </div>
      <div class="band">
        <p class="band-head">Sie können Ihr<br>Schocktrauma auflösen!</p>
        <p class="band-copy">Befreien Sie sich von den Nachwirkungen der Erfahrung und erleben Sie ein unbeschwerteres, freieres Sein.</p>
      </div>
      <div class="photo photo--beach" role="img" aria-label="Foto: Frau läuft mit ausgebreiteten Armen am Strand, Möwen fliegen auf"></div>
      <div class="foot">www.ruhe-anker.de</div>
    </article>
  </section>

  <section class="spread spread--inside">
    <article class="panel panel--inside panel--intro">
      <div class="frame"></div>
      <div class="inside-photo" role="img" aria-label="Foto: Coachin im Gespräch mit einer Klientin in hellem Raum"></div>
      <div class="copy">
        <h2>Hier eine Überschrift?</h2>
        <p class="lead">Sie haben Schlimmes erlebt und es sitzt Ihnen noch in den Knochen, hängt Ihnen nach, holt Sie ein, triggert Sie…? Sie erleben Albträume, Flashbacks, fühlen sich blockiert, verletzt, gebremst, beschämt, schuldig, überschattet, wie im Nebel, zerbrochen…?</p>
        <p>Egal, wie „groß“ oder „klein“ die Verletzung (griechisch: Trauma) war, lassen Sie nicht zu, dass sie Ihr Leben bestimmt, Sie beeinträchtigt, Sie davon abhält, Dinge zu tun, die Sie gerne tun würden.</p>
        <p>Sie brauchen nicht darauf zu warten, dass „die Zeit alle Wunden heilt“… Sie können jetzt sofort etwas tun, um die Verbindung zwischen dem Ereignis und den Mustern zu entkoppeln, die automatisch im Gehirn und Körper gestartet werden, sobald Sie etwas daran erinnert, es also einen Auslöser oder Trigger gibt.</p>
        <p>Dies gelingt mit der Anwendung der Anker Release Technik – einer Methode, die durch eine Kombination aus Klopf-Akupressur und auditiv-visuellen-motorischen Reizen neuronale Veränderungen im Gehirn bewirkt. Neuronale Muster, die durch das Trauma entstanden sind, werden gelöst und neu konditioniert.</p>
        <p class="lead">Das Geschehene wird zu einer normalen Erinnerung und löst keine Symptome mehr aus.</p>
      </div>
      <div class="inside-foot"></div>
    </article>

    <article class="panel panel--inside panel--detail-a">
      <div class="frame"></div>
      <div class="inside-photo" role="img" aria-label="Foto: Klientin legt die Hand auf die Brust, Coachin hört zu"></div>
      <div class="copy">
        <h2>Was macht ART so einzigartig?</h2>
        <ul class="bullets">
          <li>Der ART-Prozess ist sehr sanft. Eine Sitzung mit ART ist in der Regel wenig belastend, wodurch das Retraumatisierungsrisiko sehr gering ist.</li>
          <li>Die Technik ist so konzipiert, dass schon früh im Prozess im sicheren Abstand vom Fühlen gearbeitet wird. Hierdurch braucht es wenig stabilisierende Vorarbeit.</li>
          <li>ART ist ein relativ schneller Prozess. Die meisten Schocktraumata lassen sich im Rahmen einer Sitzung lösen.</li>
          <li>Die erleichternde Wirkung ist sofort spürbar.</li>
          <li>Basierend auf jahrelangen Erfahrungen von Linnea Calloway und vieler ART-Anwender/innen weltweit, wirkt eine genau nach dem Protokoll durchgeführte Sitzung nachhaltig und braucht in der Regel keine Folgesitzungen oder sonstige Nachbearbeitung.</li>
          <li>ART eignet sich sowohl für Erwachsene als auch für Kinder aller kultureller und religiöser Hintergründe.</li>
          <li>Die Technik kann auf alle belastenden Erinnerungen, die einen Schock- oder Schreckmoment enthalten, angewandt werden.</li>
          <li>Dabei ist es unerheblich, wie lange das Erlebte zurückliegt. Es muss nur eine bewusste Erinnerung in Form von Gesehenem oder Gehörtem vorhanden sein.</li>
        </ul>
      </div>
      <div class="inside-foot"></div>
    </article>

    <article class="panel panel--inside panel--detail-b">
      <div class="frame"></div>
      <div class="inside-photo" role="img" aria-label="Foto: Coachin führt mit erhobener Hand eine Klopfübung an der Stirn der Klientin an"></div>
      <div class="copy">
        <h2>Was macht ART so einzigartig?</h2>
        <ul class="bullets">
          <li>Der ART-Prozess ist sehr sanft. Eine Sitzung mit ART ist in der Regel wenig belastend, wodurch das Retraumatisierungsrisiko sehr gering ist.</li>
          <li>Die Technik ist so konzipiert, dass schon früh im Prozess im sicheren Abstand vom Fühlen gearbeitet wird. Hierdurch braucht es wenig stabilisierende Vorarbeit.</li>
          <li>ART ist ein relativ schneller Prozess. Die meisten Schocktraumata lassen sich im Rahmen einer Sitzung lösen.</li>
          <li>Die erleichternde Wirkung ist sofort spürbar.</li>
          <li>Basierend auf jahrelangen Erfahrungen von Linnea Calloway und vieler ART-Anwender/innen weltweit, wirkt eine genau nach dem Protokoll durchgeführte Sitzung nachhaltig und braucht in der Regel keine Folgesitzungen oder sonstige Nachbearbeitung.</li>
          <li>ART eignet sich sowohl für Erwachsene als auch für Kinder aller kultureller und religiöser Hintergründe.</li>
          <li>Die Technik kann auf alle belastenden Erinnerungen, die einen Schock- oder Schreckmoment enthalten, angewandt werden.</li>
          <li>Dabei ist es unerheblich, wie lange das Erlebte zurückliegt. Es muss nur eine bewusste Erinnerung in Form von Gesehenem oder Gehörtem vorhanden sein.</li>
        </ul>
      </div>
      <div class="inside-foot"></div>
    </article>
  </section>

</div>
</body>
</html>
```